The homepage of a website

This is a simple project that should take from you a few minutes as what is needed is the design of the homepage only, the details are in the attached zip file

Please note that KLVTA board required a special tailored design where they got some parts from the different posted designs, if you are interested please follow the instructions in the below URL and submit your new updated designs as per the instructions (P.S. I will mark the project as guaranteed as an assurance to all of you)

http://qorvinworks.example/Projects/KLVTA/Design.jpg
Updates

Please note that KLVTA board required a special tailored design where they got some parts from the different posted designs, if you are interested please follow the instructions in the below URL and submit your new updated designs as per the instructions (P.S. I will mark the project as guaranteed as an assurance to all of you) http://qorvinworks.example/Projects/KLVTA/Design.jpg

```html
<!DOCTYPE html>
<html lang="en">
<head>
<meta charset="utf-8">
<title>KLVTA — Home</title>
<link href="https://fonts.googleapis.com/css2?family=PT+Sans:wght@400;700&family=PT+Sans+Narrow:wght@700&family=Roboto:wght@400;500&display=swap" rel="stylesheet">
<style>
:root{
  --blue:#1d4b8c;
  --blue-dark:#163d74;
  --navy-band:#1f2c44;
  --green:#7cbb2f;
  --orange:#f7941d;
  --date:#e0531f;
  --red:#d8262e;
  --ink:#333;
  --muted:#666;
  --light:#f6f6f6;
  --line:#e3e3e3;
  --beige:#f3ece2;
  --dark-tile:#2a2a2a;
}
*{box-sizing:border-box;margin:0;padding:0}
html,body{width:1200px;height:2659px;overflow:hidden}
body{position:relative;background:#fff;font-family:"Roboto",Arial,sans-serif;color:var(--ink)}
.abs{position:absolute}
h1,h2,h3,h4{font-weight:400}

/* header */
.site-header{left:0;top:0;width:1200px;height:163px;background:#fafafa}
.brand{left:172px;top:30px;display:flex;align-items:center;gap:20px}
.brand-mark{width:104px;height:104px;border-radius:50%;background:#e9eef5;border:3px solid var(--blue)}
.brand-name{font-family:"PT Sans",sans-serif;font-weight:700;font-size:36px;color:var(--blue);line-height:1}
.brand-sub{font-family:"PT Sans",sans-serif;font-weight:700;font-size:13px;color:var(--blue);margin-top:6px;width:170px;line-height:1.3}
.lang{left:842px;top:50px;font-size:13px;color:#222;letter-spacing:.5px}
.lang svg{vertical-align:middle;margin-left:10px}
.social-dots{left:940px;top:45px;display:flex;gap:7px}
.social-dots span{width:25px;height:25px;border-radius:50%}
.search{left:815px;top:92px;width:213px;height:32px;border:1px solid #ddd;background:#fff;font-size:11px;color:#888;padding:9px 0 0 12px}
.search svg{position:absolute;right:10px;top:9px}

/* nav */
.main-nav{left:0;top:163px;width:1200px;height:55px;background:linear-gradient(#2355a0,var(--blue-dark))}
.main-nav a{position:absolute;top:18px;font-family:"PT Sans",sans-serif;font-size:16px;color:#dfe7f3;text-decoration:none}
.main-nav a.active{color:#fff;font-weight:700}
.main-nav i{position:absolute;top:12px;width:1px;height:32px;background:rgba(255,255,255,.12)}

/* hero */
.hero{left:0;top:218px;width:1200px;height:491px;background:linear-gradient(180deg,#6d8fb8 0%,#9fb6cf 30%,#b98a4e 58%,#8a5a2a 100%)}
.hero-title{left:186px;top:398px;font-family:"PT Sans Narrow",sans-serif;font-weight:700;font-size:48px;color:#fff}
.hero-text{left:186px;top:463px;font-family:"Roboto",sans-serif;font-weight:500;font-size:21px;line-height:29px;color:#fff;width:340px}
.hero-btn{left:186px;top:539px;width:170px;height:42px;background:var(--blue);color:#fff;font-size:16px;text-align:center;line-height:42px;border-radius:2px}
.hero-arrow{top:450px;width:32px;height:32px;border-radius:50%;background:rgba(40,40,40,.55)}

/* about */
.about{left:0;top:709px;width:1200px;height:243px;background:var(--light)}
.about-emblem{left:172px;top:733px;width:194px;height:194px;border-radius:50%;background:#e9eef5;border:3px solid #cdd9e8;display:flex;align-items:center;justify-content:center}
.about-emblem b{font-family:"PT Sans",sans-serif;font-size:30px;color:var(--blue)}
.about-title{left:422px;top:728px;font-family:"PT Sans",sans-serif;font-size:40px;color:#333}
.about-sub{left:422px;top:787px;font-size:17px;color:#333}
.about-text{left:422px;top:827px;width:606px;font-size:12.5px;line-height:21px;color:#555}

/* features */
.feature{top:1000px;width:300px;text-align:center}
.feature-icon{width:128px;height:128px;border:4px solid var(--green);border-radius:50%;margin:0 auto;display:flex;align-items:center;justify-content:center}
.feature h3{font-family:"PT Sans",sans-serif;font-size:18px;margin-top:26px;color:#333}
.feature p{font-size:12.5px;line-height:21px;color:#666;margin-top:10px;padding:0 22px}
.feature-divider{top:1028px;width:1px;height:215px;background:var(--line)}

/* registration band */
.reg-band{left:0;top:1299px;width:1200px;height:325px;background:linear-gradient(180deg,#1a2840 0%,#2b3850 55%,#5b4a35 100%)}
.reg-title{left:172px;top:1328px;font-family:"PT Sans Narrow",sans-serif;font-weight:700;font-size:25px;color:#fff}
.reg-input{left:172px;width:245px;height:32px;background:#fff;border-radius:2px;font-size:10px;color:#777;padding:10px 0 0 10px}
.reg-btn{left:172px;top:1551px;width:245px;height:36px;background:var(--orange);color:#fff;font-size:15px;text-align:center;line-height:36px;border-radius:2px}
.info-card{top:1329px;width:268px;height:259px;background:#fff;padding:7px}
.info-card .photo{height:135px}
.info-card h4{font-size:16px;color:#333;margin:18px 0 0 7px}
.info-card p{font-size:11.5px;line-height:20px;color:#666;margin:8px 7px 0}

/* calendar */
.calendar{left:172px;top:1671px;width:269px;height:270px;background:var(--beige);box-shadow:0 2px 4px rgba(0,0,0,.2)}
.cal-head{height:43px;background:var(--blue);color:#fff;font-size:16px;text-align:center;line-height:43px;position:relative}
.cal-head span{position:absolute;top:0;width:40px;height:43px;background:var(--blue-dark)}
.cal-grid{display:grid;grid-template-columns:repeat(7,1fr);padding:10px 8px 0;row-gap:0}
.cal-grid div{height:34px;font-size:11px;text-align:center;line-height:34px;color:#333}
.cal-grid .wd{height:22px;line-height:22px;font-size:8px;color:#555;font-weight:500}
.cal-grid .sat{color:var(--orange)}
.cal-grid .out{color:#aaa}
.cal-grid .today,.cal-grid .mark{width:28px;height:28px;line-height:28px;margin:3px auto 0;border-radius:50%;color:#fff}
.cal-grid .mark{background:var(--red)}
.cal-grid .today{background:#3fae3f}

/* events */
.events-title{left:475px;top:1662px;font-family:"PT Sans",sans-serif;font-size:23px;color:#333}
.event-arrow{top:1665px;width:20px;height:20px;border-radius:50%}
.event{top:1707px;width:170px}
.event .photo{height:151px}
.event .date{font-size:15px;color:var(--date);margin-top:21px}
.event p{font-size:11px;line-height:20px;color:#555;margin-top:8px}

/* tiles */
.tile{top:1987px;width:286px;height:317px;text-align:center}
.tile .photo{height:230px}
.tile h3{font-family:"PT Sans",sans-serif;font-size:20px;color:#222;margin-top:10px}
.tile p{font-size:11.5px;line-height:21px;color:#444;margin-top:4px;padding:0 24px}
.tile.dark{background:var(--dark-tile)}
.tile.dark h3,.tile.dark p{color:#fff}

/* footer */
.footer-strip{left:0;top:2357px;width:1200px;height:27px;background:#ebe8e1}
.site-footer{left:0;top:2384px;width:1200px;height:216px;background:#f6f6f6}
.f-col{top:2412px}
.f-col h4{font-size:15px;color:var(--blue);font-weight:500;letter-spacing:.3px}
.f-col p,.f-col li{font-size:11.5px;line-height:20px;color:#555;list-style:none}
.f-divider{top:2410px;width:1px;height:165px;background:var(--line)}
.news-input{width:237px;height:39px;border:1px solid #ddd;background:#fff;font-size:12px;color:#555;padding:12px 0 0 14px;margin-top:20px}
.subscribe{width:80px;height:30px;background:var(--blue-dark);color:#fff;font-size:12px;text-align:center;line-height:30px;border-radius:3px;margin-top:14px}
.social-list li{display:flex;align-items:center;gap:12px;height:28px}
.social-list i{width:10px;height:10px;border-radius:50%;background:#222}
.bottom-bar{left:0;top:2600px;width:1200px;height:59px;background:var(--blue);color:#fff;font-size:11px;text-align:center;line-height:59px}
</style>
</head>
<body>

<header class="site-header abs">
  <div class="brand abs">
    <div class="brand-mark"></div>
    <div>
      <div class="brand-name">KLVTA</div>
      <div class="brand-sub">KLVTA Society of Reconstructive Surgeons</div>
    </div>
  </div>
  <div class="lang abs">ENGLISH<svg width="10" height="6" viewBox="0 0 10 6"><path d="M1 1l4 4 4-4" fill="none" stroke="#222" stroke-width="1.5"/></svg></div>
  <div class="social-dots abs"><span style="background:#3b5fa8"></span><span style="background:#2ea6dd"></span><span style="background:#d0312d"></span></div>
  <div class="search abs">Search<svg width="12" height="12" viewBox="0 0 12 12"><circle cx="5" cy="5" r="3.6" fill="none" stroke="#999" stroke-width="1.4"/><path d="M7.7 7.7L11 11" stroke="#999" stroke-width="1.4"/></svg></div>
</header>

<nav class="main-nav abs">
  <a class="active" style="left:172px">Home</a><i style="left:236px"></i>
  <a style="left:260px">Board</a><i style="left:322px"></i>
  <a style="left:346px">History</a><i style="left:418px"></i>
  <a style="left:441px">Members</a><i style="left:526px"></i>
  <a style="left:551px">Activities</a><i style="left:640px"></i>
  <a style="left:663px">Laws</a><i style="left:718px"></i>
  <a style="left:742px">Journal</a><i style="left:815px"></i>
  <a style="left:838px">Downloads</a><i style="left:935px"></i>
  <a style="left:959px">Contact</a>
</nav>

<section class="hero abs" role="img" aria-label="Photograph of desert pyramids under a cloudy blue sky"></section>
<h1 class="hero-title abs">Sed ut perspiciatis</h1>
<p class="hero-text abs">Lorem ipsum dolor sit amet, consectetur adipiscing elit, sed do</p>
<div class="hero-btn abs">More Information</div>
<div class="hero-arrow abs" style="left:50px"><svg width="32" height="32" viewBox="0 0 32 32"><path d="M19 10l-6 6 6 6" fill="none" stroke="#fff" stroke-width="2.5"/></svg></div>
<div class="hero-arrow abs" style="left:1122px"><svg width="32" height="32" viewBox="0 0 32 32"><path d="M13 10l6 6-6 6" fill="none" stroke="#fff" stroke-width="2.5"/></svg></div>

<section class="about abs"></section>
<div class="about-emblem abs"><b>KLVTA</b></div>
<h2 class="about-title abs">About KLVTA</h2>
<p class="about-sub abs">Message from The President of KLVTA</p>
<p class="about-text abs">Lorem ipsum dolor sit amet, consectetur adipiscing elit, sed do eiusmod tempor incididunt ut labore et dolore magna aliqua. Ut enim ad minim veniam, quis nostrud exercitation ullamco laboris nisi ut aliquip ex ea commodo consequat. Duis aute irure dolor in reprehenderit in voluptate velit esse cillum dolore eu fugiat nulla pariatur. Excepteur sint occaecat cupidatat non proident, sunt in culpa qui</p>

<div class="feature abs" style="left:141px">
  <div class="feature-icon"><svg width="50" height="50" viewBox="0 0 50 50"><circle cx="25" cy="15" r="10" fill="#7cbb2f"/><path d="M6 46c0-12 8-18 19-18s19 6 19 18z" fill="#7cbb2f"/></svg></div>
  <h3>KLVTA History</h3>
  <p>Lorem ipsum dolor sit amet, consetur adipiscing elit. Vivamus luctus urna sed urna ultricies ac</p>
</div>
<div class="feature-divider abs" style="left:454px"></div>
<div class="feature abs" style="left:465px">
  <div class="feature-icon"><svg width="56" height="56" viewBox="0 0 56 56"><path d="M50 6L6 26l18 6 6 18z" fill="none" stroke="#7cbb2f" stroke-width="4" stroke-linejoin="round"/><path d="M50 6L24 32" stroke="#7cbb2f" stroke-width="4"/></svg></div>
  <h3>KLVTA Board</h3>
  <p>Lorem ipsum dolor sit amet, consetur adipiscing elit. Vivamus luctus urna sed urna ultricies ac</p>
</div>
<div class="feature-divider abs" style="left:775px"></div>
<div class="feature abs" style="left:773px">
  <div class="feature-icon"><svg width="64" height="56" viewBox="0 0 64 56"><circle cx="15" cy="14" r="8" fill="#7cbb2f"/><circle cx="49" cy="14" r="8" fill="#7cbb2f"/><circle cx="32" cy="20" r="9" fill="#7cbb2f"/><path d="M2 40c0-9 6-14 13-14s10 4 11 7l-4 7z" fill="#7cbb2f"/><path d="M62 40c0-9-6-14-13-14s-10 4-11 7l4 7z" fill="#7cbb2f"/><path d="M14 52c0-12 8-19 18-19s18 7 18 19z" fill="#7cbb2f"/></svg></div>
  <h3>Members Ships</h3>
  <p>Lorem ipsum dolor sit amet, consetur adipiscing elit. Vivamus luctus urna sed urna ultricies ac</p>
</div>

<section class="reg-band abs" role="img" aria-label="Dimmed photograph of pyramids under a dark evening sky"></section>
<h2 class="reg-title abs">Members Registration</h2>
<div class="reg-input abs" style="top:1377px">Name</div>
<div class="reg-input abs" style="top:1420px">E - Mail Address</div>
<div class="reg-input abs" style="top:1462px">Phone</div>
<div class="reg-input abs" style="top:1505px">Address</div>
<div class="reg-btn abs">Sign Up Now</div>
<article class="info-card abs" style="left:457px">
  <div class="photo" role="img" aria-label="Photograph of a doctor talking with an elderly patient" style="background:linear-gradient(135deg,#dfe6ec,#9fb0c0)"></div>
  <h4>Patients education information</h4>
  <p>Lorem ipsum dolor sit amet, consectetur adipiscing elit, sed do eiusmod tempor incididunt ut labore et dolore</p>
</article>
<article class="info-card abs" style="left:762px">
  <div class="photo" role="img" aria-label="Illustration of a DNA helix beside a researcher in a lab coat" style="background:linear-gradient(135deg,#bfe3ef,#5fb3cf)"></div>
  <h4>Research information</h4>
  <p>Lorem ipsum dolor sit amet, consectetur adipiscing elit, sed do eiusmod tempor incididunt ut labore et dolore</p>
</article>

<aside class="calendar abs">
  <div class="cal-head"><span style="left:0"></span>November 2014<span style="right:0"></span>
    <svg class="abs" style="left:14px;top:15px" width="10" height="13" viewBox="0 0 10 13"><path d="M8 1L2 6.5 8 12" fill="none" stroke="#fff" stroke-width="1.6"/></svg>
    <svg class="abs" style="right:14px;top:15px" width="10" height="13" viewBox="0 0 10 13"><path d="M2 1l6 5.5L2 12" fill="none" stroke="#fff" stroke-width="1.6"/></svg>
  </div>
  <div class="cal-grid">
    <div class="wd">MON</div><div class="wd">TUE</div><div class="wd">WED</div><div class="wd">THU</div><div class="wd">FRI</div><div class="wd sat">SAT</div><div class="wd sat">SUN</div>
    <div class="out">30</div><div>1</div><div>2</div><div>3</div><div>4</div><div>5</div><div><div class="mark">6</div></div>
    <div>7</div><div>8</div><div>9</div><div>10</div><div>11</div><div>12</div><div>13</div>
    <div>14</div><div>15</div><div>16</div><div>17</div><div><div class="today">18</div></div><div>19</div><div>20</div>
    <div>21</div><div>22</div><div>23</div><div>24</div><div>25</div><div>26</div><div>27</div>
    <div>28</div><div>29</div><div>30</div><div>31</div><div class="out">1</div><div class="out">2</div><div class="out">3</div>
  </div>
</aside>

<h2 class="events-title abs">Upcoming Events</h2>
<div class="event-arrow abs" style="left:979px;background:var(--blue)"><svg width="20" height="20" viewBox="0 0 20 20"><path d="M12 6l-4 4 4 4" fill="none" stroke="#fff" stroke-width="2"/></svg></div>
<div class="event-arrow abs" style="left:1006px;background:#222"><svg width="20" height="20" viewBox="0 0 20 20"><path d="M8 6l4 4-4 4" fill="none" stroke="#fff" stroke-width="2"/></svg></div>
<article class="event abs" style="left:475px">
  <div class="photo" role="img" aria-label="Photograph of students studying together at a table" style="background:linear-gradient(135deg,#e8e6e2,#9aa8b8)"></div>
  <div class="date">Jan 03, 2015</div>
  <p>Lorem ipsum dolor sit amet, nsectetuer adipiscing elit, sed diam</p>
</article>
<article class="event abs" style="left:666px">
  <div class="photo" role="img" aria-label="Photograph of a person looking through a telescope over a city" style="background:linear-gradient(180deg,#c9c4bb,#6f6a64)"></div>
  <div class="date">Jan 03, 2015</div>
  <p>Lorem ipsum dolor sit amet, nsectetuer adipiscing elit, sed diam</p>
</article>
<article class="event abs" style="left:860px">
  <div class="photo" role="img" aria-label="Photograph of a nurse attending to an elderly patient" style="background:linear-gradient(135deg,#eef2f4,#4f8fc6)"></div>
  <div class="date">Jan 03, 2015</div>
  <p>Lorem ipsum dolor sit amet, nsectetuer adipiscing elit, sed diam</p>
</article>

<article class="tile abs" style="left:172px">
  <div class="photo" role="img" aria-label="Illustration of a scientist working with a digital interface" style="background:linear-gradient(135deg,#cfe6f6,#2f86c8)"></div>
  <h3>Scientific Activities</h3>
  <p>Lorem ipsum dolor sit amet, consectetur ipiscing elit, sed do eiusmod tempor</p>
</article>
<article class="tile dark abs" style="left:457px">
  <div class="photo" role="img" aria-label="Historic painting of scholars reading manuscripts" style="background:linear-gradient(135deg,#c9672a,#6e3516)"></div>
  <h3>KLVTA Journal</h3>
  <p>Lorem ipsum dolor sit amet, consectetur ipiscing elit, sed do eiusmod tempor</p>
</article>
<article class="tile abs" style="left:743px">
  <div class="photo" role="img" aria-label="Photograph of students writing in a classroom" style="background:linear-gradient(135deg,#e9d9cf,#b25a6e)"></div>
  <h3>E-Learning information</h3>
  <p>Lorem ipsum dolor sit amet, consectetur ipiscing elit, sed do eiusmod tempor</p>
</article>

<div class="footer-strip abs"></div>
<footer class="site-footer abs"></footer>
<div class="f-col abs" style="left:172px">
  <h4>NEWSLETTER SIGNUP</h4>
  <p style="margin-top:10px">Sign up for our newsletter and<br>get the latest news.</p>
  <div class="news-input">E -Mail</div>
  <div class="subscribe">subscribe</div>
</div>
<div class="f-divider abs" style="left:454px"></div>
<div class="f-col abs" style="left:507px">
  <h4>LINKS</h4>
  <ul style="margin-top:12px"><li>Home</li><li>Board</li><li>History</li><li>Members</li><li>Activities</li><li>Laws</li></ul>
</div>
<div class="f-divider abs" style="left:611px"></div>
<div class="f-col abs" style="left:674px">
  <h4>GET IN TOUCH</h4>
  <p style="margin-top:12px">3200 KLVTA works. 58<br>Linden Vale, NC 27500</p>
  <p style="margin-top:14px">Toll free:&nbsp;&nbsp;(555) 014-2290</p>
  <p style="margin-top:12px;color:#333">info@klvta.example</p>
</div>
<div class="f-divider abs" style="left:876px"></div>
<div class="f-col abs" style="left:948px">
  <h4>SOCIAL</h4>
  <ul class="social-list" style="margin-top:8px"><li><i></i>Friendly</li><li><i></i>Chirper</li><li><i></i>Pinwall</li><li><i></i>Tubecast</li></ul>
</div>
<div class="bottom-bar abs">©2014 - 2015&nbsp; klvta.example.,All Rights Reserved.</div>

</body>
</html>
```